COVID-19 Related Signage for Hotel

Need to create new COVID-19 related signage utilizing our brand assets. Please use screenshots for copy/direction. essentially duplicate the screenshots but with our logo/branding.

All brand assets have been uploaded and examples of signage content. Pictures are not necessary but you can add them if you want similar to the examples attached.

Sign requirements

sign 1. Text "Hand Sanitizer Station" can add graphic
sign 2. Text "Protect Yourself" duplicate copy in the attached pictures
sign 3. Text "Face Mask Required" can add graphic
sign 4. Text "Face Covering Do's and Don'ts with text from "Face-covering checklist.jpg" REMOVE BWT logo or website or 3 face mask graphics
sign 5. Text "Maintain 6 Foot Distance" This sign will be printed and placed on the ground for guests to know where to stand in queue. Would prefer a circular Design. sign 6. Text "Wet, Lather, Scrub, Rinse, Dry" similar to screenshots attached.

ALL signs should have same look and feel throughout utilizing our brand graphics, logo, colors, and guidelines.

Target Market(s)

Hotel Guests

Industry/Entity Type

Hotel

Font styles to use
Sans Serif

Requirements
Must have
• Cohesive, unified branding look and feel

Should not have
• any use of the word "COVID-19" or Coronavirus.

```html
<!DOCTYPE html>
<html lang="en">
<head>
<meta charset="utf-8">
<title>Protect Yourself – High Ridge Lodge</title>
<link rel="stylesheet" href="https://fonts.googleapis.com/css2?family=Montserrat:wght@500;600&display=swap">
<style>
  :root {
    --teal: #00b0b9;
    --teal-light: #5fd0d6;
    --orange: #ff7a00;
    --ink: #2f2f2f;
    --white: #ffffff;
  }
  * { margin: 0; padding: 0; box-sizing: border-box; }
  html, body { width: 902px; height: 1200px; overflow: hidden; background: var(--teal); }
  .sign {
    position: relative;
    width: 902px; height: 1200px;
    background: var(--teal);
    font-family: "Montserrat", Arial, sans-serif;
  }
  .sign-title {
    position: absolute; left: 92px; top: 82px;
    color: var(--white);
    font-weight: 500;
    font-size: 74px;
    line-height: 84px;
    letter-spacing: 1px;
  }
  .brand {
    position: absolute; left: 633px; top: 83px;
    width: 152px; height: 152px;
    border-radius: 50%;
    background: var(--orange);
    border: 2px solid var(--white);
    display: flex; align-items: center; justify-content: center;
    text-align: center;
  }
  .brand-name {
    color: var(--white);
    font-weight: 500;
    font-size: 21px;
    line-height: 25px;
  }
  .panel {
    position: absolute; left: 91px; top: 307px;
    width: 715px; height: 771px;
    background: var(--white);
  }
  .rule-item {
    position: absolute; left: 20px;
    display: flex; align-items: flex-start;
  }
  .rule-icon {
    width: 180px; height: 180px;
    flex: none;
    display: flex; align-items: center; justify-content: center;
  }
  .rule-icon--dark { background: var(--ink); }
  .rule-icon--teal { background: radial-gradient(circle at 50% 50%, var(--teal-light) 0%, var(--teal) 70%); }
  .rule-icon--orange { background: var(--orange); }
  .rule-text {
    margin: 22px 0 0 35px;
    font-weight: 600;
    font-size: 42px;
    line-height: 54px;
    color: var(--ink);
    letter-spacing: 0.5px;
    white-space: nowrap;
  }
  .accent { color: var(--orange); }
  .item-distance { top: 24px; }
  .item-handwash { top: 296px; }
  .item-mask { top: 559px; }
  .site-url {
    position: absolute; left: 0; right: 0; top: 1111px;
    text-align: center;
    color: var(--white);
    font-weight: 500;
    font-size: 36px;
    line-height: 44px;
    letter-spacing: 1px;
  }
</style>
</head>
<body>
<main class="sign">
  <h1 class="sign-title">PROTECT<br>YOURSELF</h1>

  <div class="brand"><span class="brand-name">high ridge<br>lodge</span></div>

  <section class="panel">
    <div class="rule-item item-distance">
      <div class="rule-icon rule-icon--dark">
        <svg width="156" height="132" viewBox="0 0 170 140" fill="none" stroke="#fff" stroke-width="4" stroke-linecap="round" stroke-linejoin="round">
          <path d="M50 12 H120 M58 4 L50 12 L58 20 M112 4 L120 12 L112 20"/>
          <circle cx="35" cy="30" r="14"/>
          <path d="M12 70 Q12 50 35 50 Q58 50 58 70 V95 M12 70 V95 M22 70 V134 H48 V70 M35 86 V134"/>
          <circle cx="135" cy="30" r="14"/>
          <path d="M112 70 Q112 50 135 50 Q158 50 158 70 V95 M112 70 V95 M122 70 V134 H148 V70 M135 86 V134"/>
        </svg>
      </div>
      <p class="rule-text"><span class="accent">MAINTAINING</span><br>SOCIAL DISTANCING</p>
    </div>

    <div class="rule-item item-handwash">
      <div class="rule-icon rule-icon--teal" role="img" aria-label="Icon of two hands washing with soap bubbles"></div>
      <p class="rule-text"><span class="accent">HAND</span> WASHING<br>PROCEDURES</p>
    </div>

    <div class="rule-item item-mask">
      <div class="rule-icon rule-icon--orange">
        <svg width="172" height="106" viewBox="0 0 180 110" fill="none" stroke="#fff" stroke-width="5" stroke-linecap="round" stroke-linejoin="round">
          <path d="M30 20 Q90 4 150 20 V90 Q90 106 30 90 Z"/>
          <path d="M30 30 Q4 30 4 55 Q4 80 30 80 M150 30 Q176 30 176 55 Q176 80 150 80"/>
          <path d="M48 36 H132 M62 55 H118 M48 74 H132"/>
        </svg>
      </div>
      <p class="rule-text"><span class="accent">MASK</span><br>REQUIREMENT</p>
    </div>
  </section>

  <p class="site-url">WWW.HIGHRIDGELODGE.COM</p>
</main>
</body>
</html>
```